pathology learning flashcard template graphic design .

Creative designs for 2 sides of the flashcards to include colorful sectioning and font sizes that will make it easy to use in studying.

```html
<!DOCTYPE html>
<html lang="en">
<head>
<meta charset="utf-8">
<title>Pathology Flashcard – Gastrointestinal Case 0001</title>
<link rel="stylesheet" href="https://fonts.googleapis.com/css2?family=Roboto:wght@400;500;700;900&display=swap">
<style>
  :root{
    --bg:#eaeaea;
    --card:#ffffff;
    --accent:#f44a6d;
    --accent-dark:#e83a60;
    --ink:#111111;
    --muted:#2a2a2a;
    --photo-a:#7a7570;
    --photo-b:#3c3a3a;
  }
  *{box-sizing:border-box;margin:0;padding:0}
  html,body{width:1200px;height:1200px;overflow:hidden}
  body{background:var(--bg);font-family:"Roboto",Arial,sans-serif;color:var(--ink);position:relative}
  .card{position:absolute;left:224px;width:752px;background:var(--card);box-shadow:0 6px 14px rgba(0,0,0,.22)}
  .card--front{top:61px;height:523px}
  .card--back{top:613px;height:528px}

  .card__band{position:absolute;left:0;top:0;width:100%;height:160px}
  .card__title{position:absolute;left:40px;top:46px;color:#fff;font-weight:700;font-size:33px;letter-spacing:.3px}
  .card__subtitle{position:absolute;left:40px;top:96px;color:#fff;font-weight:500;font-size:22px;letter-spacing:.4px}
  .patient-photo{position:absolute;left:592px;top:40px;width:109px;height:142px;
    background:linear-gradient(170deg,var(--photo-a),var(--photo-b));box-shadow:8px 8px 0 #9b9b9b}

  .case-text{position:absolute;left:40px;top:206px;width:672px;font-size:17px;line-height:20.5px}
  .case-text p{margin-bottom:20px}
  .answer-bar{position:absolute;left:0;top:445px;width:86px;height:38px;background:var(--accent)}
  .answers{position:absolute;left:104px;top:446px;display:grid;grid-template-columns:300px 300px;row-gap:2px;font-weight:700;font-size:17px}
  .answers span:nth-child(even){padding-left:0}

  .topic-title{position:absolute;left:40px;top:28px;color:var(--accent);font-weight:700;font-size:35px}
  .col{position:absolute;top:80px;width:310px}
  .col--left{left:40px}
  .col--right{left:384px;width:320px}
  .fact{margin-bottom:14px}
  .fact h3{font-size:17px;font-weight:700;line-height:19px}
  .fact p{font-size:13.4px;line-height:16.3px;color:var(--muted)}
  .col--right .fact{margin-bottom:24px}

  .explain-bar{position:absolute;left:0;top:368px;width:37px;height:107px;background:var(--accent)}
  .explain{position:absolute;left:56px;top:370px;width:650px}
  .explain h3{font-size:17px;font-weight:700;line-height:19px}
  .explain p{font-size:13.4px;line-height:16.3px;color:var(--muted)}
  .sources{position:absolute;right:42px;top:487px;font-size:9.5px;color:var(--muted)}
</style>
</head>
<body>

<section class="card card--front">
  <svg class="card__band" viewBox="0 0 752 160" preserveAspectRatio="none" aria-hidden="true">
    <path d="M0 0 H752 V98 C640 108 560 160 420 150 C300 142 200 125 0 140 Z" fill="var(--accent)"/>
  </svg>
  <h1 class="card__title">GASTROINTESTINAL</h1>
  <h2 class="card__subtitle">PATHOLOGY CASE ID 0001</h2>
  <div class="patient-photo" role="img" aria-label="Portrait photo of the patient"></div>

  <div class="case-text">
    <p>50-year-old woman comes to the clinic because she has difficulty swallowing for the past few months. She says symptoms have been worsening.</p>
    <p>She also complains of cough, mostly at night and in fear of choking, has stopped eating many foods, losing about 12 lbs in the past 3 months. Past medical history is unremarkable. Vital signs are normal and physical exam is unremarkable. Chest x-ray with demonstrates an air-fluid level, while manometry shows absent relaxation of the lower esophageal sphincter during swallowing.</p>
    <p>What is the most likely diagnosis?</p>
  </div>

  <div class="answer-bar"></div>
  <div class="answers">
    <span>A) GERD</span><span>C) Achalasia</span>
    <span>B) Barret Esophagus</span><span>D) Eosinophilic esophagitis</span>
  </div>
</section>

<section class="card card--back">
  <h2 class="topic-title">Achalasia</h2>

  <div class="col col--left">
    <div class="fact"><h3>Definition:</h3><p>Motility disorder where esophageal relaxation is impaired in the lower esophageal sphincter (LES).</p></div>
    <div class="fact"><h3>Etiology/Pathology:</h3><p>Destruction of inhibitory neurons in the Auerbach plexus. Loss of peristalsis in the lower esophageal sphincter (Lower-two thirds of the esophagus).</p></div>
    <div class="fact"><h3>P/E and Symptoms:</h3><p>Dysphagia that is progressive, regurgitation, weight-loss, dry cough, chest pain, GERD, esophageal perforation, squamous cell carcinoma, aspiration pneumonia.</p></div>
  </div>

  <div class="col col--right">
    <div class="fact"><h3>Dx:</h3><p>Barium swallow will show ‘bird’s beak’ and esophageal dilation. Manometry will present with increased resting lower esophageal sphincter pressure. Endoscopy will usually present with normal mucosa and LES dilation, and in some cases residual material such as undigested food particles may be present.</p></div>
    <div class="fact"><h3>Rx:</h3><p>First line of treatment are nitrates, calcium channel blockers, and Botulinum toxin injection in the LES. Long term management options include esophageal dilation with pneumatic balloon and myotomy.</p></div>
  </div>

  <div class="explain-bar"></div>
  <div class="explain">
    <h3>C- Achalasia</h3>
    <p>Symptoms and studies suggestive of achalasia. Patient’s manometry presents with no relaxation of the lower esophageal sphincter during swallowing. Patient also complains of dysphagia and is unable to swallow properly, leading to weight loss. Patient has no past infection or inflammation, ruling out eosinophilic esophagitis. Patient does not have chronic GERD, eliminating the possibility of Barrett esophagus, in which at least 5 years of acid reflux are beforehand to develop columnar metaplasia.</p>
  </div>
  <p class="sources">Sources:Hartwell Clinical Guide;Pocket Pathology Reference;StudyMed Notes;ClinRef Online</p>
</section>

</body>
</html>
```